Unique business card design

Boutique coastal hotel suites - in need of clever stand out business card I have uploaded the logo that I had created through brand loft I want something that is clever and stands out from everyone else - 418 Marrowind Lane brinehaven Alaska 99528 phone or text 907 -561-8204 www.tidewrenlodgeinn.com

Target Market(s)

Men and woman

Industry/Entity Type

Boutique coastal hotel

Contact Information for Business Card

Tidewren Lodge brinehaven Alaska tidewren_lodge@kelpmail.com

Requirements
Must have
• Classy - clever -bold 907-561-8204 call or text

```html
<!DOCTYPE html>
<html lang="en">
<head>
<meta charset="utf-8">
<title>Tidewren Lodge – Business Cards</title>
<link href="https://fonts.googleapis.com/css2?family=Montserrat:wght@400;500;700&display=swap" rel="stylesheet">
<style>
  :root {
    --backdrop: #d9d9d7;
    --paper: #f1efeb;
    --charcoal: #33322f;
    --navy: #3d5a78;
    --sun: #f2d64b;
    --ink: #1d1d1b;
    --light-text: #eceae5;
  }
  * { box-sizing: border-box; margin: 0; padding: 0; }
  html, body {
    width: 1200px; height: 801px; overflow: hidden;
    background: var(--backdrop);
    font-family: "Montserrat", sans-serif;
  }
  .stage {
    position: relative; width: 1200px; height: 801px;
    display: flex; align-items: center; justify-content: center; gap: 60px;
  }
  .card {
    position: relative; width: 525px; height: 300px;
    background: var(--paper);
    border-bottom: 4px solid var(--sun);
    box-shadow: 0 10px 24px rgba(0,0,0,.18);
    overflow: hidden;
  }
  .wordmark {
    display: flex; align-items: center; gap: 12px;
    color: var(--navy); font-weight: 700; font-size: 34px;
    letter-spacing: 2px; text-transform: uppercase; white-space: nowrap;
  }
  .wordmark .mark-square {
    width: 22px; height: 22px; background: var(--navy); flex: none;
  }
  .rule { position: absolute; height: 3px; background: var(--ink); }

  /* Front */
  .card--front .wordmark { position: absolute; left: 70px; top: 52px; }
  .card--front .rule { left: 70px; top: 118px; width: 370px; }
  .info-band {
    position: absolute; left: 0; right: 0; top: 138px; bottom: 0;
    background: var(--charcoal);
    display: flex; align-items: center; padding: 0 28px 0 60px;
  }
  .person { width: 170px; text-align: right; padding-right: 18px; }
  .person__name { color: var(--sun); font-weight: 700; font-size: 19px; line-height: 1.2; white-space: nowrap; }
  .person__title { color: var(--light-text); font-size: 12.5px; margin-top: 4px; white-space: nowrap; }
  .divider { width: 2px; height: 92px; background: var(--sun); flex: none; }
  .contact { padding-left: 18px; color: var(--light-text); font-size: 11.5px; line-height: 1.65; white-space: nowrap; }
  .contact__row { display: flex; align-items: center; gap: 7px; }
  .contact__row svg { width: 11px; height: 11px; flex: none; }

  /* Back */
  .card--back .wordmark { position: absolute; left: 78px; top: 110px; }
  .card--back .rule { left: 78px; top: 176px; width: 370px; }
</style>
</head>
<body>
<main class="stage">
  <section class="card card--front">
    <div class="wordmark"><span class="mark-square"></span>Tidewren Lodge</div>
    <div class="rule"></div>
    <div class="info-band">
      <div class="person">
        <p class="person__name">Marcus Ellery</p>
        <p class="person__title">Managing Director</p>
      </div>
      <div class="divider"></div>
      <div class="contact">
        <p class="contact__address">418 Marrowind Lane</p>
        <p class="contact__address">brinehaven Alaska 99528</p>
        <p class="contact__row">
          <svg viewBox="0 0 12 12"><path d="M3 1 L5 3.5 L4 4.8 Q5 7 7.2 8 L8.5 7 L11 9 L9.8 11 Q4.5 10.5 1 3 Z" fill="var(--sun)"/></svg>
          907 -561-8204
        </p>
        <p class="contact__row">
          <svg viewBox="0 0 12 12"><rect x="0.5" y="2" width="11" height="8" fill="var(--sun)"/><path d="M0.5 2 L6 6.5 L11.5 2" stroke="var(--charcoal)" stroke-width="1" fill="none"/></svg>
          info@tidewrenlodgeinn.com
        </p>
        <p class="contact__row">
          <svg viewBox="0 0 12 12"><circle cx="6" cy="6" r="5.3" fill="none" stroke="var(--sun)" stroke-width="1.2"/><ellipse cx="6" cy="6" rx="2.3" ry="5.3" fill="none" stroke="var(--sun)" stroke-width="1"/><path d="M0.7 6 H11.3" stroke="var(--sun)" stroke-width="1"/></svg>
          www.tidewrenlodgeinn.com
        </p>
      </div>
    </div>
  </section>

  <section class="card card--back">
    <div class="wordmark"><span class="mark-square"></span>Tidewren Lodge</div>
    <div class="rule"></div>
  </section>
</main>
</body>
</html>
```